WordPress Website Design for Multi-Brand Aviation Group (Unified Branding System)

Project Overview:
We are seeking a professional, modern WordPress website design for an aviation-focused umbrella company that owns and operates multiple subsidiary businesses. The goal is to create a cohesive visual system that clearly communicates that each company operates under the same parent organization, while still allowing each brand to maintain a slightly distinct identity.
This is not just a single website design—we are looking for a scalable design framework that can be applied across multiple aviation-related businesses.
Objectives:
- Establish a consistent, recognizable brand identity across all company websites
Clearly communicate the relationship between the parent company and its subsidiaries
-bCreate a clean, high-end corporate aviation aesthetic
- Ensure all designs are SEO-friendly and optimized for performance
- Allow flexibility for future expansion (additional subsidiaries)
- Target Audience:
- Corporate aviation clients
- Charter customers
- Students wishing to receive flight training
- Aircraft owners and operators
- Turbine aircraft training to meet insurance requirements
- Business professionals and high-net-worth individuals
- Aviation industry partners
Design Direction & Style:
We are looking for a premium, professional aviation feel—think clean, modern, and high-trust. The design should reflect the standards of corporate aviation: precision, safety, and sophistication.
Key style notes:
Minimalist but impactful layout
High-quality aviation photography (jets, interiors, operations, global travel)
Subtle motion/interaction (hover effects, transitions)
Clear typography hierarchy for readability and professionalism
Branding Requirements:
Incorporate the primary colors of the parent company logo across all designs
Website Structure (Core Pages):
Design a system that includes:
Home Page with the following links:
- About / Company Overview
- Aircraft Management
- Aircraft Acquisition
- Charter
- Pilot Services
- Trip Support
- Contact Page
Site should further include:
- Mobile-first responsive design
- Fast-loading, performance-optimized layouts
SEO & Technical Considerations:
- Design should support high-level SEO implementation:
- Clean layout structure that translates well to semantic HTML
- Proper heading hierarchy (H1, H2, H3)
- Space for keyword-rich content without clutter
- Optimized image placement (with alt text capability)
- Fast load times (lightweight design approach)
- Compatibility with WordPress SEO plugins (e.g., Yoast or Rank Math)
WordPress Requirements:
- Design should be easily built using WordPress (preferred builders: Elementor, Gutenberg, or similar)
- Reusable templates for scalability across multiple sites
- Easy for non-developers to update text and images
- Modular components (blocks/sections that can be reused across pages and sites)
- Navigation & UX:
- Simple, intuitive navigation
- Sticky header preferred
Style guide including:
- Colors
- Fonts
- Button styles
- Layout system
- Designs similar to high-end corporate aviation, private jet charter, or luxury service brands are preferred—clean, sharp, and premium without being overly flashy.
What We Want to Avoid:
- Overly busy layouts
- Generic templates with no brand identity
- Outdated or “stock” looking aviation designs
- Poor mobile responsiveness
Additional Notes:
We are building a long-term brand system, not just a one-off website. There is potential for ongoing work as we expand additional subsidiary sites.
We value designers who understand branding consistency across multiple business units and can create a scalable, professional system.
Include the attached main company logo "Tarnwell Aviation Group" and the "Member FLTC" logo on the main page.
1 page

```html
<!DOCTYPE html>
<html lang="en">
<head>
<meta charset="utf-8">
<title>Tarnwell Aviation Group — Excellence in Aviation</title>
<link href="https://fonts.googleapis.com/css2?family=Poppins:wght@400;500;600&family=Inter:wght@400;500&display=swap" rel="stylesheet">
<style>
:root{
  --navy:#0a2c57;
  --navy-deep:#061d3d;
  --blue:#0a5bb0;
  --accent:#1e6bff;
  --ink:#0d1117;
  --text:#2b3340;
  --muted:#5b6472;
  --line:#d5d9e0;
  --footer:#0f1a2b;
  --white:#ffffff;
}
*{box-sizing:border-box;margin:0;padding:0}
html,body{width:1200px;height:3762px;overflow:hidden;background:var(--white)}
body{font-family:"Poppins",sans-serif;color:var(--ink);position:relative}
.abs{position:absolute}
.brand-name{font-family:"Poppins",sans-serif;font-weight:600;color:var(--navy);font-size:15px;line-height:17px;width:150px;letter-spacing:.5px}

/* header */
.site-header{position:absolute;left:0;top:0;width:1200px;height:80px}
.site-header .brand-name{left:44px;top:22px}
.nav a{position:absolute;top:28px;font-size:15px;color:var(--muted);text-decoration:none;font-family:"Inter",sans-serif}
.nav a.active{color:var(--blue);font-weight:500;text-decoration:underline;text-underline-offset:5px}
.btn{display:flex;align-items:center;justify-content:center;gap:8px;border-radius:6px;font-weight:500;text-decoration:none;color:var(--white);font-family:"Poppins",sans-serif}
.btn-primary{background:linear-gradient(180deg,#0b4a93,var(--navy-deep))}
.btn-outline{border:1.5px solid rgba(255,255,255,.85);background:transparent}
.header-cta{left:1038px;top:19px;width:117px;height:38px;font-size:15px;font-family:"Inter",sans-serif;font-weight:400}

/* hero */
.hero{left:39px;top:80px;width:1122px;height:478px;border-radius:18px;overflow:hidden;
  background:radial-gradient(ellipse at 50% 78%,#2c6e86 0%,#123b55 22%,#07182c 55%,#040c18 100%)}
.hero h1{position:absolute;top:140px;width:100%;text-align:center;color:var(--white);font-weight:600;font-size:46px;letter-spacing:1.5px}
.hero p{position:absolute;top:206px;left:356px;width:410px;text-align:center;color:#e6ecf3;font-size:19px;line-height:30px}
.hero .b1{left:386px;top:332px;width:210px;height:46px;font-size:13.5px}
.hero .b2{left:608px;top:332px;width:127px;height:46px;font-size:13.5px}

/* about */
.about h2{left:48px;top:668px;font-size:37px;font-weight:600;line-height:51px;letter-spacing:1px;width:520px}
.about .copy{left:48px;top:786px;width:560px;font-size:16.6px;line-height:33.5px;color:var(--text)}
.about .copy p+p{margin-top:14px}
.about .learn{left:48px;top:1063px;width:134px;height:41px;font-size:13.5px}
.about .photo{left:628px;top:666px;width:533px;height:441px;border-radius:14px;
  background:linear-gradient(135deg,#5a6068 0%,#2b3036 45%,#8a97a6 75%,#3a3f46 100%)}

/* services */
.services-title{left:0;top:1212px;width:1200px;text-align:center;font-size:37px;font-weight:600;letter-spacing:1px}
.divider{left:0;top:1310px;width:1200px;height:1px;background:#eceef1}
.card{position:absolute;width:353px}
.card .media{position:relative;height:234px;border-radius:6px;overflow:hidden}
.card .media::after{content:"";position:absolute;inset:0;background:linear-gradient(180deg,rgba(0,0,0,0) 55%,rgba(0,0,0,.55) 100%)}
.card .label{position:absolute;left:14px;bottom:22px;display:flex;align-items:center;gap:11px;z-index:1;color:var(--white);font-family:"Inter",sans-serif;font-weight:500;font-size:18px}
.icon{width:34px;height:34px;border-radius:8px;background:var(--accent);display:flex;align-items:center;justify-content:center}
.card p{margin-top:22px;font-family:"Inter",sans-serif;font-size:14px;line-height:22px;color:var(--text)}

/* cta band */
.cta{left:0;top:2057px;width:1200px;height:276px;background:linear-gradient(180deg,#0a5bb0 0%,#0a3f7d 55%,#0a2a52 100%);text-align:center;color:var(--white)}
.cta h2{margin-top:44px;font-size:34px;font-weight:600;letter-spacing:1.5px}
.cta p{margin-top:16px;font-size:16.5px;line-height:34px}
.cta .btn{position:absolute;left:520px;top:187px;width:160px;height:48px;font-size:13.5px}
.stray-chevron{left:1104px;top:2366px}

/* contact */
.contact-title{left:0;top:2440px;width:1200px;text-align:center;font-size:37px;font-weight:600;letter-spacing:1px}
.contact-sub{left:0;top:2506px;width:1200px;text-align:center;font-size:17px;color:var(--text)}
.field-label{position:absolute;font-family:"Inter",sans-serif;font-size:20px;font-weight:500;color:#2a3444}
.input{position:absolute;border:1.5px solid var(--line);border-radius:5px;font-family:"Inter",sans-serif;font-size:23px;color:#6d7580;padding-left:25px;display:flex;align-items:center;background:var(--white)}
.input.select{color:var(--ink);padding-left:31px}
.input.area{align-items:flex-start;padding-top:20px}
.submit{left:73px;top:3364px;width:1060px;height:49px;font-size:13.5px}

/* footer */
.site-footer{left:0;top:3551px;width:1200px;height:211px;background:var(--footer);color:#c4cbd6;font-family:"Inter",sans-serif}
.site-footer .brand-name{position:absolute;left:88px;top:22px;color:#2f74d6;width:160px}
.site-footer .tag{position:absolute;left:88px;top:68px;width:190px;font-size:11.5px;line-height:17px}
.f-col{position:absolute;top:7px}
.f-col h4{font-size:13px;font-weight:500;color:var(--white);margin-bottom:10px}
.f-col li{list-style:none;font-size:11.5px;line-height:23px}
.social{margin-top:10px;font-size:13px;display:flex;gap:20px}
.legal{position:absolute;top:172px;font-size:11.5px}
</style>
</head>
<body>

<header class="site-header">
  <div class="abs brand-name">Tarnwell Aviation Group</div>
  <nav class="nav">
    <a class="active" href="#" style="left:306px">Home</a>
    <a href="#" style="left:386px">Services</a>
    <a href="#" style="left:484px">Aircraft Management</a>
    <a href="#" style="left:679px">Aircraft Acquisition</a>
    <a href="#" style="left:856px">Charter</a>
  </nav>
  <a class="abs btn btn-primary header-cta" href="#">Contact Us</a>
</header>

<section class="abs hero" role="img" aria-label="Business jet on a night runway, lit from below">
  <h1>Excellence in Aviation</h1>
  <p>Delivering precision, safety, and sophistication across all facets of corporate aviation management</p>
  <a class="abs btn btn-primary b1" href="#">Explore Our Services
    <svg width="10" height="12" viewBox="0 0 10 12"><path d="M3 1l5 5-5 5" fill="none" stroke="#fff" stroke-width="1.8"/></svg></a>
  <a class="abs btn btn-outline b2" href="#">Get In Touch</a>
</section>

<section class="about">
  <h2 class="abs">Multi-Brand Aviation Excellence</h2>
  <div class="abs copy">
    <p>Tarnwell Aviation Group serves as the umbrella organization for a family of premier aviation companies, each specializing in distinct aspects of corporate aviation while maintaining our unwavering commitment to excellence.</p>
    <p>Our integrated approach allows us to offer comprehensive aviation solutions, from aircraft acquisition and management to charter services and pilot training, all under one trusted brand.</p>
  </div>
  <a class="abs btn btn-primary learn" href="#">Learn More
    <svg width="10" height="12" viewBox="0 0 10 12"><path d="M3 1l5 5-5 5" fill="none" stroke="#fff" stroke-width="1.8"/></svg></a>
  <div class="abs photo" role="img" aria-label="Pilot adjusting overhead switches in a jet cockpit"></div>
</section>

<h2 class="abs services-title">Our Services</h2>
<div class="abs divider"></div>

<article class="card" style="left:41px;top:1320px">
  <div class="media" role="img" aria-label="Business jet parked on an airport apron" style="background:linear-gradient(180deg,#7d93ab 0%,#b9c3cc 55%,#5d646c 100%)">
    <div class="label"><span class="icon"><svg width="18" height="18" viewBox="0 0 24 24" fill="none" stroke="#fff" stroke-width="2"><circle cx="12" cy="12" r="3"/><path d="M12 2v3M12 19v3M2 12h3M19 12h3M4.9 4.9l2.1 2.1M17 17l2.1 2.1M4.9 19.1L7 17M17 7l2.1-2.1"/></svg></span>Aircraft Management</div>
  </div>
  <p>Comprehensive management solutions for your aviation assets with precision and professionalism.</p>
</article>
<article class="card" style="left:422px;top:1320px">
  <div class="media" role="img" aria-label="Private jet on a runway at dusk" style="background:linear-gradient(180deg,#2c4446 0%,#1b2b2d 60%,#3c3a36 100%)">
    <div class="label"><span class="icon"><svg width="18" height="18" viewBox="0 0 24 24" fill="none" stroke="#fff" stroke-width="2"><path d="M3 4h3l2 11h11l2-8H7"/><circle cx="9" cy="20" r="1.5"/><circle cx="18" cy="20" r="1.5"/></svg></span>Aircraft Acquisition</div>
  </div>
  <p>Expert guidance in selecting and acquiring the perfect aircraft for your operational needs.</p>
</article>
<article class="card" style="left:804px;top:1320px">
  <div class="media" role="img" aria-label="Leather seats inside a private jet cabin" style="background:linear-gradient(90deg,#6b4a2c 0%,#c08f5d 30%,#d9c3a4 50%,#b9844f 70%,#6a4829 100%)">
    <div class="label"><span class="icon"><svg width="18" height="18" viewBox="0 0 24 24" fill="none" stroke="#fff" stroke-width="2"><path d="M2 16l8-3 5-8 2 1-3 7 6-2 1 2-17 6z"/></svg></span>Charter</div>
  </div>
  <p>Premium charter services delivering unparalleled comfort and flexibility for your travel requirements.</p>
</article>

<article class="card" style="left:41px;top:1642px">
  <div class="media" role="img" aria-label="Pilot wearing a headset in a dim cockpit" style="background:linear-gradient(135deg,#2d3b4a 0%,#121a24 55%,#070b10 100%)">
    <div class="label"><span class="icon"><svg width="18" height="18" viewBox="0 0 24 24" fill="none" stroke="#fff" stroke-width="2"><circle cx="9" cy="8" r="3.5"/><path d="M2 20c0-4 3-6 7-6s7 2 7 6M16 4.5a3.5 3.5 0 010 7M18 14c2.5.6 4 2.6 4 6"/></svg></span>Pilot Services</div>
  </div>
  <p>Professional pilot training and services meeting the highest standards of aviation excellence.</p>
</article>
<article class="card" style="left:422px;top:1642px">
  <div class="media" role="img" aria-label="Jet instrument panel and flight controls" style="background:linear-gradient(180deg,#a4a7ab 0%,#3c3d3f 35%,#1a1b1c 70%,#4a4644 100%)">
    <div class="label"><span class="icon"><svg width="18" height="18" viewBox="0 0 24 24" fill="none" stroke="#fff" stroke-width="2"><path d="M4 14v-2a8 8 0 0116 0v2"/><rect x="3" y="14" width="4" height="6" rx="1"/><rect x="17" y="14" width="4" height="6" rx="1"/></svg></span>Trip Support</div>
  </div>
  <p>Seamless coordination and support for every aspect of your aviation operations.</p>
</article>
<article class="card" style="left:804px;top:1642px">
  <div class="media" role="img" aria-label="Business jet flying against a blue sky" style="background:linear-gradient(180deg,#0d4f8e 0%,#2b77b8 50%,#5d9acb 100%)">
    <div class="label"><span class="icon"><svg width="18" height="18" viewBox="0 0 24 24" fill="none" stroke="#fff" stroke-width="2"><path d="M12 22s-7-7-7-12a7 7 0 0114 0c0 5-7 12-7 12z"/><circle cx="12" cy="10" r="2.5"/></svg></span>Global Operations</div>
  </div>
  <p>Worldwide aviation solutions with local expertise and international reach.</p>
</article>

<section class="abs cta">
  <h2>Ready to Elevate Your Aviation Experience?</h2>
  <p>Connect with our team to discuss how Tarnwell Aviation Group<br>can support your aviation needs</p>
  <a class="btn btn-outline" href="#">Contact Us Today</a>
</section>
<svg class="abs stray-chevron" width="16" height="10" viewBox="0 0 16 10"><path d="M2 2l6 5 6-5" fill="none" stroke="#222" stroke-width="1.6"/></svg>

<h2 class="abs contact-title">Get in Touch</h2>
<p class="abs contact-sub">Let us know how we can assist with your aviation requirements</p>

<form>
  <label class="field-label" style="left:69px;top:2608px">First Name</label>
  <div class="input" style="left:69px;top:2650px;width:512px;height:73px">John</div>
  <label class="field-label" style="left:618px;top:2608px">Last Name</label>
  <div class="input" style="left:618px;top:2650px;width:513px;height:73px">Smith</div>
  <label class="field-label" style="left:69px;top:2762px">Email</label>
  <div class="input" style="left:69px;top:2803px;width:1062px;height:75px">john.smith@company.com</div>
  <label class="field-label" style="left:69px;top:2915px">Service Interest</label>
  <div class="input select" style="left:69px;top:2957px;width:1062px;height:70px">Select a service</div>
  <label class="field-label" style="left:69px;top:3065px">Message</label>
  <div class="input area" style="left:69px;top:3107px;width:1062px;height:217px">Tell us about your aviation needs...</div>
  <a class="abs btn btn-primary submit" href="#">Submit
    <svg width="10" height="12" viewBox="0 0 10 12"><path d="M3 1l5 5-5 5" fill="none" stroke="#fff" stroke-width="1.8"/></svg></a>
</form>

<footer class="abs site-footer">
  <div class="brand-name">Tarnwell Aviation Group</div>
  <p class="tag">Excellence in corporate aviation management and services</p>
  <div class="f-col" style="left:345px;top:7px"><h4>Services</h4><ul><li>Aircraft Management</li><li>Aircraft Acquisition</li><li>Charter</li><li>Pilot Services</li></ul></div>
  <div class="f-col" style="left:603px;top:7px"><h4>Company</h4><ul><li>About Us</li><li>Our Companies</li><li>Careers</li><li>Contact</li></ul></div>
  <div class="f-col" style="left:860px;top:7px"><h4>Connect</h4><ul><li>Phone: (555) 240-8816</li><li>Email: info@tarnwellaviation.com</li></ul>
    <div class="social"><span>Linkline</span><span>Chirpfeed</span></div></div>
  <p class="legal" style="left:88px">© 2026 Tarnwell Aviation Group. All rights reserved.</p>
  <p class="legal" style="left:908px">Privacy Policy</p>
  <p class="legal" style="left:1002px">Terms of Service</p>
</footer>

</body>
</html>
```